Natural Cosmetics need a Packaging Design

We need a PACKAGING design for labels on hand/body wash bottles and soap paper boxes.
We target at high end markets.
We expect a contemporary and trendy design.
We don't need a separate logo. The brand name "Va Mirel" acts as the logo.
We want a modern and classic font for "Va Mirel".
Please see attached pictures for packaging samples.

Industry/Entity Type

Cosmetics

Requirements
Should not have
• a separate logo from the brand name

```html
<!DOCTYPE html>
<html lang="en">
<head>
<meta charset="utf-8">
<title>Va Mirel – Soap Box Dieline</title>
<link rel="stylesheet" href="https://fonts.googleapis.com/css2?family=Playfair+Display:wght@700&family=Gelasio:ital@1&display=swap">
<style>
  :root {
    --bg-light: #f6f7f7;
    --bg-dark: #e6e7e9;
    --panel-blush: #f3dfca;
    --paper: #ffffff;
    --cut-line: #3a3a3a;
    --ink: #111111;
    --floor-line: #8a8a8a;
  }
  html, body {
    margin: 0;
    padding: 0;
    width: 1132px;
    height: 1200px;
    overflow: hidden;
  }
  .canvas {
    width: 1132px;
    height: 1200px;
    background: linear-gradient(90deg, var(--bg-light), var(--bg-dark));
  }
  .dieline { display: block; }
  .cut { stroke: var(--cut-line); stroke-width: 1.2; }
  .flap { fill: var(--paper); }
  .panel-blush { fill: var(--panel-blush); }
  .panel-white { fill: var(--paper); }
  .label-ground { fill: var(--paper); }
  .label-frame { fill: none; stroke: var(--ink); stroke-width: 2; }
  .floor { stroke: var(--floor-line); stroke-width: 1.5; }
  .brand-name {
    font-family: "Playfair Display", serif;
    font-weight: 700;
    font-size: 24px;
    letter-spacing: 7px;
    fill: var(--ink);
  }
  .product-line {
    font-family: "Gelasio", serif;
    font-style: italic;
    font-size: 18px;
    fill: var(--ink);
  }
</style>
</head>
<body>
<main class="canvas">
  <svg class="dieline" width="1132" height="1200" viewBox="0 0 1152 1221" xmlns="http://www.w3.org/2000/svg">
    <!-- top tuck flap -->
    <path class="flap cut" d="M230,213 L230,205 Q230,138 300,138 L690,138 Q760,138 760,205 L760,213 Z"/>
    <!-- top panel -->
    <rect class="panel-blush cut" x="230" y="213" width="530" height="166"/>
    <!-- front panel -->
    <rect class="panel-blush cut" x="230" y="379" width="530" height="529"/>
    <!-- side panel -->
    <rect class="panel-white cut" x="760" y="379" width="185" height="529"/>
    <!-- side dust flap -->
    <polygon class="flap cut" points="778,379 800,362 816,257 911,266 931,346 945,358 945,379"/>
    <!-- bottom flaps -->
    <polygon class="flap cut" points="230,908 230,940 252,965 274,1048 373,1048 388,927 404,909"/>
    <polygon class="flap cut" points="766,908 766,940 788,965 809,1048 908,1048 924,927 940,909"/>

    <!-- front label -->
    <g class="front-label">
      <rect class="label-ground" x="340" y="461" width="320" height="319"/>
      <rect class="label-frame" x="355" y="475" width="290" height="290"/>
      <line class="label-frame" x1="355" y1="621" x2="645" y2="621"/>
      <text class="brand-name" x="503" y="562" text-anchor="middle">VA MIREL</text>
      <text class="product-line" x="500" y="683" text-anchor="middle">Hand Soap</text>
      <text class="product-line" x="500" y="714" text-anchor="middle">Made in France</text>
    </g>

    <line class="floor" x1="0" y1="1219" x2="1152" y2="1219"/>
  </svg>
</main>
</body>
</html>
```